Software company specialized in data analytics and professional services

We need a landing page design for our business. It should include our logo design. It should have multiple sections :
- stylish head
- what we do (data analytics software, professional services)
- contact form

Target Market(s)

Companies, B2B

Industry/Entity Type

Data

Number of Pages Required

1 page

Font styles to use
Sans Serif

Requirements
Must have
• Dark theme
Should not have
• Gradients on buttons

```html
<!DOCTYPE html>
<html lang="en">
<head>
<meta charset="utf-8">
<title>NORTHGRID – Data Analysis Company</title>
<link href="https://fonts.googleapis.com/css2?family=Poppins:wght@400;500;600;700;800&display=swap" rel="stylesheet">
<style>
:root{
  --black:#000;
  --white:#fff;
  --pink:#e8168f;
  --magenta:#d61ad0;
  --purple:#8a12e6;
  --violet:#6a0fd0;
  --topbar:#1d2d4f;
  --footer:#1c1448;
  --grey:#bdbdbd;
  --star:#e3b23c;
}
*{margin:0;padding:0;box-sizing:border-box}
html,body{width:1200px;height:3804px;overflow:hidden;background:var(--black)}
body{font-family:"Poppins",sans-serif;color:var(--white);position:relative}
.abs{position:absolute}
.btn{position:absolute;display:flex;align-items:center;justify-content:center;border-radius:16px;font-size:15px;font-weight:500;letter-spacing:.3px}
.btn-pink{background:var(--pink);color:var(--white)}
.btn-white{background:var(--white);color:var(--black)}
.eyebrow{font-size:15px;font-weight:500;letter-spacing:.3px}
.eyebrow::after{content:"";display:block;width:56px;height:3px;background:var(--purple);margin-top:4px}
.center{left:0;width:1200px;text-align:center}
.center .eyebrow::after{margin:4px auto 0}
.h-section{font-weight:800;font-size:46px;line-height:1.1}
.small-p{font-size:12px;line-height:20px;color:#d8d8d8}

/* top bar */
.topbar{top:0;left:0;width:1200px;height:34px;background:var(--topbar);font-size:15px}
.topbar span{position:absolute;top:7px;display:flex;align-items:center;gap:10px}
.nav{top:34px;left:0;width:1200px;height:70px;background:var(--black)}
.brand{position:absolute;left:7px;top:14px;font-size:38px;font-weight:700;color:var(--magenta);letter-spacing:1px}
.nav-links{position:absolute;top:33px;left:374px;display:flex;gap:30px;font-size:15px;font-weight:500}
.nav-links a{color:var(--white);text-decoration:none}

/* hero */
.hero{top:104px;left:0;width:1200px;height:596px;background:linear-gradient(120deg,#3a3634 0%,#5b4a40 45%,#2d2a2a 100%)}
.hero-shade{top:104px;left:0;width:1200px;height:596px;background:rgba(0,0,0,.35)}
.hero-title{top:240px;font-size:59px;font-weight:800;line-height:70px}
.hero-text{top:394px;font-size:14px;line-height:24px}
.dots{top:652px;left:505px;width:130px;height:24px}

/* about */
.about-frame{left:125px;top:779px;width:406px;height:356px}
.about-title{left:617px;top:826px;font-size:44px;font-weight:800;line-height:52px}

/* banner */
.banner{top:1210px;left:0;width:1200px;height:203px;background:linear-gradient(90deg,#c21683 0%,#b82bb0 45%,#a13ad0 75%,#9b42e0 100%)}
.banner-title{left:131px;top:1252px;font-size:46px;font-weight:800;line-height:52px}

/* services */
.card{position:absolute;top:1632px;width:221px;height:266px;border:2px solid;border-image:linear-gradient(180deg,var(--pink),var(--violet)) 1}
.card h3{position:absolute;left:34px;top:126px;font-size:22px;font-weight:600;line-height:26px}
.card svg{position:absolute;left:32px;top:42px}
.plus{position:absolute;left:92px;bottom:-20px;width:36px;height:36px;background:linear-gradient(180deg,var(--pink),var(--purple));display:flex;align-items:center;justify-content:center;font-size:30px;font-weight:700;line-height:1}

/* professional band */
.pro{top:2000px;left:0;width:1200px;height:406px;background:linear-gradient(110deg,#2a1e5c 0%,#26306e 50%,#1a5c8a 100%)}
.tabs{top:2340px;left:223px;width:760px;height:66px}

/* testimonials */
.t-card{position:absolute;top:2635px;width:477px;height:229px;border:2px solid var(--purple);overflow:hidden}
.t-card .name{position:absolute;left:170px;top:52px;font-size:22px;font-weight:600}
.t-card .stars{position:absolute;left:170px;top:88px;color:var(--star);font-size:20px;letter-spacing:3px}
.t-card p{position:absolute;left:170px;top:124px;width:270px;font-size:11px;line-height:18px;color:#cfcfcf}

/* contact */
.contact-photo{top:2999px;left:0;width:576px;height:415px;background:linear-gradient(135deg,#6b4a3a 0%,#a77a5c 45%,#c9b39c 100%)}
.field{position:absolute;border:1.5px solid var(--pink);background:var(--white);color:#777;font-size:16px;padding:8px 16px}

/* footer */
.footer{top:3414px;left:0;width:1200px;height:390px;background:var(--footer)}
.f-head{font-size:21px;font-weight:600;letter-spacing:.5px}
.f-list{font-size:15px}
.f-list li{list-style:none;display:flex;align-items:center;gap:12px;height:35px}
.f-list li::before{content:"";width:12px;height:12px;border-radius:50%;background:var(--pink)}
.social{position:absolute;top:3736px;width:28px;height:28px;border-radius:50%;background:var(--pink)}
</style>
</head>
<body>

<div class="abs topbar">
  <span style="left:14px">
    <svg width="20" height="20" viewBox="0 0 24 24"><path d="M6.6 10.8c1.4 2.8 3.8 5.2 6.6 6.6l2.2-2.2c.3-.3.7-.4 1-.2 1.1.4 2.3.6 3.6.6.6 0 1 .4 1 1V20c0 .6-.4 1-1 1C10.6 21 3 13.4 3 4c0-.6.4-1 1-1h3.5c.6 0 1 .4 1 1 0 1.3.2 2.5.6 3.6.1.3 0 .7-.2 1z" fill="#fff"/></svg>
    (+10)555 0199 24
  </span>
  <span style="left:258px">
    <svg width="20" height="16" viewBox="0 0 24 18"><rect x="1" y="3" width="22" height="14" rx="1" fill="#fff"/><path d="M1 4l11 7 11-7" stroke="#1d2d4f" stroke-width="2" fill="none"/></svg>
    hello@northgrid.example
  </span>
</div>

<header class="abs nav">
  <div class="brand">NORTHGRID</div>
  <nav class="nav-links">
    <a href="#">HOME</a><a href="#">ABOUT</a><a href="#">SERVICES</a><a href="#" style="margin-left:6px">WHY CHOOSE US</a><a href="#">TESTIMONIALS</a>
  </nav>
  <div class="btn btn-pink" style="left:1016px;top:25px;width:138px;height:32px">CONTACT US</div>
</header>

<section>
  <div class="abs hero" role="img" aria-label="Photo of a smiling team working together in a bright office"></div>
  <div class="abs hero-shade"></div>
  <h1 class="abs center hero-title">Best Data<br>Analysis Company</h1>
  <p class="abs center hero-text">Lorem ipsum dolor sit amet, consectetur adipiscing elit,<br>sed do eiusmod tempor incididunt ut labore<br>et dolore magna aliqua.</p>
  <div class="btn btn-pink" style="left:509px;top:502px;width:139px;height:30px">CONTACT US</div>
  <svg class="abs dots" viewBox="0 0 130 24"><circle cx="12" cy="12" r="10" fill="#fff"/><circle cx="59" cy="12" r="10" fill="none" stroke="#fff" stroke-width="3"/><circle cx="112" cy="12" r="10" fill="#fff"/></svg>
</section>

<section>
  <svg class="abs about-frame" viewBox="0 0 406 356">
    <defs><linearGradient id="fr" x1="0" y1="1" x2="1" y2="0"><stop offset="0" stop-color="#e8168f"/><stop offset="1" stop-color="#8a12e6"/></linearGradient></defs>
    <path d="M0 30a30 30 0 0 1 30-30h346a30 30 0 0 1 30 30v100h-25v96h25v100a30 30 0 0 1-30 30H30a30 30 0 0 1-30-30V226h25v-96H0z" fill="url(#fr)"/>
  </svg>
  <div class="abs" role="img" aria-label="Photo of a colleague reviewing dashboards on a laptop" style="left:152px;top:806px;width:352px;height:302px;border-radius:18px;background:linear-gradient(135deg,#cfc6bd 0%,#8e8b8c 50%,#2a3040 100%)"></div>
  <div class="abs eyebrow" style="left:617px;top:791px">ABOUT US</div>
  <h2 class="abs about-title">Best Data<br>Analysis Company</h2>
  <p class="abs small-p" style="left:617px;top:950px;width:490px">Lorem ipsum dolor sit amet, consectetur adipiscing elit, sed do eiusmod tempor incididunt ut labore et dolore magna aliqua. Ut enim ad minim veniam, quis nostrud exercitation ullamco laboris nisi ut aliquip ex ea commodo consequat. Duis aute irure dolor in reprehenderit in voluptate velit esse cillum dolore eu fugiat nulla pariatur.</p>
  <div class="btn btn-pink" style="left:617px;top:1061px;width:139px;height:30px">READ MORE</div>
</section>

<section>
  <div class="abs banner" role="img" aria-label="Photo of a customer at work tinted pink and purple"></div>
  <div class="abs" style="top:1210px;left:0;width:14px;height:203px;background:var(--pink)"></div>
  <h2 class="abs banner-title">Hundreds of Customers<br>Trust Our Digital Agency</h2>
  <div class="btn btn-white" style="left:918px;top:1297px;width:137px;height:31px">READ MORE</div>
</section>

<section>
  <div class="abs center" style="top:1478px"><span class="eyebrow" style="display:inline-block">WHAT WE DO</span></div>
  <h2 class="abs center h-section" style="top:1515px">Our Professional Services</h2>

  <div class="card" style="left:115px">
    <svg width="66" height="66" viewBox="0 0 66 66" fill="none" stroke="#e8168f" stroke-width="2.5"><rect x="2" y="4" width="50" height="40"/><path d="M2 12h50"/><circle cx="40" cy="40" r="16"/><path d="M52 52l12 12"/><path d="M32 46v-6M38 46V34M44 46v-9"/></svg>
    <h3>Data<br>Analysis</h3><div class="plus">+</div>
  </div>
  <div class="card" style="left:359px">
    <svg width="66" height="66" viewBox="0 0 66 66" fill="none" stroke="#e8168f" stroke-width="2.5"><rect x="4" y="2" width="44" height="62"/><circle cx="18" cy="16" r="7"/><path d="M30 12h12M30 18h12M10 30h32M10 36h20"/><path d="M22 58v-8M30 58V44M38 58V48M46 58V40"/></svg>
    <h3>Reporting<br>Automation</h3><div class="plus">+</div>
  </div>
  <div class="card" style="left:602px">
    <svg width="66" height="66" viewBox="0 0 66 66" fill="none" stroke="#e8168f" stroke-width="2.5"><rect x="8" y="2" width="56" height="44"/><path d="M8 10h56"/><rect x="14" y="18" width="12" height="10"/><rect x="30" y="18" width="12" height="10"/><rect x="46" y="18" width="12" height="10"/><circle cx="16" cy="50" r="9"/><circle cx="16" cy="50" r="3"/></svg>
    <h3>Data<br>Management</h3><div class="plus">+</div>
  </div>
  <div class="card" style="left:844px">
    <svg width="66" height="66" viewBox="0 0 66 66" fill="none" stroke="#e8168f" stroke-width="2.5"><rect x="4" y="2" width="40" height="58"/><path d="M12 20h14M12 28h18M12 36h14M12 44h10"/><circle cx="42" cy="36" r="16"/><path d="M34 42l6-6 4 4 8-9"/></svg>
    <h3>Financial<br>Analytics</h3><div class="plus">+</div>
  </div>
</section>

<section>
  <div class="abs pro" role="img" aria-label="Photo of an analyst at a laptop tinted navy and teal"></div>
  <h2 class="abs center h-section" style="top:2070px">Professional Services</h2>
  <p class="abs center small-p" style="top:2135px;color:#fff">Lorem ipsum dolor sit amet, consectetur adipiscing elit, sed do eiusmod tempor<br>incididunt ut labore et dolore magna aliqua. Ut enim ad minim veniam, quis nostrud<br>exercitation ullamco laboris nisi ut aliquip ex ea commodo consequat. Duis aute irure<br>dolor in reprehenderit in voluptate velit esse cillum dolore eu fugiat nulla pariatur.</p>
  <div class="btn btn-white" style="left:523px;top:2236px;width:138px;height:30px">READ MORE</div>
  <svg class="abs tabs" viewBox="0 0 760 66">
    <defs><linearGradient id="tb" x1="0" y1="0" x2="1" y2="0"><stop offset="0" stop-color="#d4168f"/><stop offset="1" stop-color="#8a12e6"/></linearGradient></defs>
    <path d="M0 0h248l22 33-22 33H0z" fill="url(#tb)"/>
    <path d="M505 0h230l25 33-25 33H505l22-33z" fill="url(#tb)"/>
    <path d="M248 0h257l22 33-22 33H248l22-33z" fill="#fff"/>
    <g font-family="Poppins, sans-serif" font-size="19" font-weight="600">
      <text x="32" y="40" fill="#fff">Business Growth</text>
      <text x="290" y="40" fill="#000">Professional Services</text>
      <text x="558" y="40" fill="#fff">Financial Advice</text>
    </g>
  </svg>
</section>

<section>
  <div class="abs center" style="top:2487px"><span class="eyebrow" style="display:inline-block">TESTIMONIALS</span></div>
  <h2 class="abs center h-section" style="top:2526px">What Client Say’s</h2>

  <div class="t-card" style="left:87px">
    <svg class="abs" style="left:0;top:0" width="477" height="229" viewBox="0 0 477 229">
      <defs><linearGradient id="tg1" x1="0" y1="1" x2="1" y2="0"><stop offset="0" stop-color="#e8168f"/><stop offset="1" stop-color="#8a12e6"/></linearGradient></defs>
      <path d="M0 0h135L30 229H0z" fill="#13206a"/>
      <path d="M30 229l60-130 95 130z" fill="url(#tg1)"/>
      <circle cx="95" cy="100" r="55" fill="#6f8fb3" role="img" aria-label="Client portrait"/>
    </svg>
    <div class="name">Daniel Reyes</div><div class="stars">★★★★★</div>
    <p>Lorem ipsum dolor sit amet, consectetur adipiscing elit, sed do eiusmod tempor incididunt ut labore et dolore magna aliqua. et enim ad minim veniam, quis nostrud</p>
  </div>
  <div class="t-card" style="left:626px">
    <svg class="abs" style="left:0;top:0" width="477" height="229" viewBox="0 0 477 229">
      <defs><linearGradient id="tg2" x1="0" y1="1" x2="1" y2="0"><stop offset="0" stop-color="#e8168f"/><stop offset="1" stop-color="#8a12e6"/></linearGradient></defs>
      <path d="M0 0h135L30 229H0z" fill="#13206a"/>
      <path d="M30 229l60-130 95 130z" fill="url(#tg2)"/>
      <circle cx="95" cy="100" r="55" fill="#6f8fb3" role="img" aria-label="Client portrait"/>
    </svg>
    <div class="name">Daniel Reyes</div><div class="stars">★★★★★</div>
    <p>Lorem ipsum dolor sit amet, consectetur adipiscing elit, sed do eiusmod tempor incididunt ut labore et dolore magna aliqua. et enim ad minim veniam, quis nostrud</p>
  </div>
</section>

<section>
  <div class="abs contact-photo" role="img" aria-label="Photo of three colleagues smiling around a laptop"></div>
  <div class="abs eyebrow" style="left:630px;top:3044px">HAVE ANY QUESTION</div>
  <h2 class="abs" style="left:632px;top:3078px;font-size:44px;font-weight:700">CONTACT US</h2>
  <div class="field" style="left:642px;top:3153px;width:239px;height:44px">Name</div>
  <div class="field" style="left:908px;top:3153px;width:239px;height:44px">Email</div>
  <div class="field" style="left:642px;top:3210px;width:239px;height:45px">Phone</div>
  <div class="field" style="left:908px;top:3210px;width:239px;height:45px">Subject</div>
  <div class="field" style="left:642px;top:3269px;width:505px;height:93px">Message</div>
</section>

<footer>
  <div class="abs footer"></div>
  <div class="abs" style="left:111px;top:3520px;font-size:34px;font-weight:700;color:var(--white)">NORTHGRID</div>
  <p class="abs" style="left:111px;top:3608px;width:270px;font-size:11px;line-height:18px;color:#e0e0e0">Lorem ipsum dolor sit amet, consectetur adipiscing elit, sed do eiusmod tempor incididunt ut labore et dolore magna aliqua. et enim ad minim veniam, quis nostrud</p>

  <div class="abs f-head" style="left:546px;top:3508px">EXPLORE</div>
  <ul class="abs f-list" style="left:546px;top:3538px"><li>Home</li><li>About</li><li>Services</li><li>Contact</li></ul>

  <div class="abs f-head" style="left:865px;top:3508px">CONTACT</div>
  <div class="abs f-list" style="left:865px;top:3554px;display:flex;align-items:center;gap:14px">
    <svg width="22" height="22" viewBox="0 0 24 24"><path d="M6.6 10.8c1.4 2.8 3.8 5.2 6.6 6.6l2.2-2.2c.3-.3.7-.4 1-.2 1.1.4 2.3.6 3.6.6.6 0 1 .4 1 1V20c0 .6-.4 1-1 1C10.6 21 3 13.4 3 4c0-.6.4-1 1-1h3.5c.6 0 1 .4 1 1 0 1.3.2 2.5.6 3.6.1.3 0 .7-.2 1z" fill="#e8168f"/></svg>(+10)555 0199 24</div>
  <div class="abs f-list" style="left:865px;top:3602px;display:flex;align-items:center;gap:14px">
    <svg width="22" height="18" viewBox="0 0 24 18"><rect x="1" y="3" width="22" height="14" rx="1" fill="#e8168f"/><path d="M1 4l11 7 11-7" stroke="#1c1448" stroke-width="2" fill="none"/></svg>hello@northgrid.example</div>
  <div class="abs f-list" style="left:868px;top:3648px;display:flex;align-items:center;gap:16px">
    <svg width="18" height="24" viewBox="0 0 18 24"><path d="M9 0a9 9 0 0 1 9 9c0 6-9 15-9 15S0 15 0 9a9 9 0 0 1 9-9z" fill="#e8168f"/><circle cx="9" cy="9" r="3.5" fill="#1c1448"/></svg>12 Harbor Lane, Eastport</div>

  <div class="abs" style="left:118px;top:3740px;font-size:10px">COpyright 2023, All Rights Reserved</div>
  <div class="social" style="left:961px"></div>
  <div class="social" style="left:1006px"></div>
  <div class="social" style="left:1052px"></div>
</footer>

</body>
</html>
```